Advertising plattform for handcraft companies

We need as design for an advertising platform for handcraft companies. The central element of the design should be a grid of 9 visible (but scrollables) boxes. In this boxes are logos of the advertising companies are shown.
Clicking a box will open es small window (like a lightbox) with further information about the company.

The main page will show a grid with the nine states of Austria. Clicking a state will show a grid with companies of this state sorted by region. Every region are represented in on line (3 boxes).

The design should be realizable as "responsive design".

Target Market(s)

- Austria
- for all customers who are looking for a plumber

Industry/Entity Type

Advertising

Requirements
Must have
• - Details shown as "lightbox"
• - Middle strip in "Companies" page should be highlighted
• - up and down scrolling funtionaltiy for "Companies" grid
• - Companies are selectable by state and region with drowdown menus (selected region will be highlighted)
• - Screen should show the elements as shown in the uploaded sketches.
Nice to have
• - Interesting wallpaper (website will advertise plumbers)
• - Nice animated effects

```html
<!DOCTYPE html>
<html lang="en">
<head>
<meta charset="utf-8">
<title>Handwerkplatz.at – Companies</title>
<link rel="stylesheet" href="https://fonts.googleapis.com/css2?family=Roboto:wght@300;400;500;700&family=Great+Vibes&display=swap">
<style>
:root{
  --backdrop:#efe6d2;
  --brand:#3a8fc4;
  --brand-text:#2f95d6;
  --accent:#e02a2a;
  --page-bg:#f1f1f1;
  --card:#ffffff;
  --ink:#333333;
  --muted:#666666;
  --bottom-bar:#e4e4e4;
  --shade:rgba(0,0,0,.6);
}
*{box-sizing:border-box;margin:0;padding:0}
html,body{width:1200px;height:1129px;overflow:hidden}
body{background:var(--backdrop);font-family:'Roboto',sans-serif;color:var(--ink);position:relative}
.site{position:absolute;left:40px;top:2px;width:858px;height:864px;transform:scale(1.305);transform-origin:0 0;background:var(--page-bg);overflow:hidden}
.header{position:absolute;left:0;top:0;width:858px;height:40px;background:var(--brand)}
.brand{position:absolute;left:58px;top:5px;display:flex;align-items:center;gap:6px;color:#fff;font-weight:700;font-size:12px}
.brand-mark{width:26px;height:26px;border-radius:50%;background:#fff}
.nav{position:absolute;right:60px;top:0;display:flex;gap:22px;height:40px}
.nav a{color:#fff;text-decoration:none;font-size:10px;font-weight:500;line-height:38px;border-bottom:2px solid transparent;padding:0 4px}
.nav a.active{border-bottom-color:#fff}
.hero{position:absolute;left:0;top:40px;width:858px;height:165px;background:linear-gradient(180deg,#2d5f86 0%,#6f93b3 45%,#c9a27c 75%,#5c6f88 100%)}
.hero h1{position:absolute;top:36px;width:100%;text-align:center;color:#fff;font-size:27px;font-weight:700}
.hero h1 .script{font-family:'Great Vibes',cursive;font-weight:400;font-size:24px}
.hero p{position:absolute;top:76px;left:130px;width:598px;text-align:center;color:#fff;font-size:10.5px;font-weight:300;line-height:17px}
.filter{position:absolute;left:201px;top:187px;width:455px;height:41px;background:#fff;border-radius:2px;display:flex;align-items:center;padding:0 11px 0 16px;gap:8px}
.filter label{color:var(--brand-text);font-size:8.5px;font-weight:500;width:38px}
.select{width:147px;height:20px;border:1px solid #ddd;font-size:8px;color:#999;line-height:18px;padding-left:8px;position:relative}
.select::after{content:"";position:absolute;right:0;top:0;width:10px;height:18px;background:#555}
.submit{margin-left:auto;width:69px;height:20px;background:var(--accent);color:#fff;font-size:9px;font-weight:700;line-height:20px;text-align:center;border-radius:2px}
.grid{position:absolute;left:73px;top:262px;width:697px;display:grid;grid-template-columns:repeat(3,225px);gap:13px 11px}
.card{height:103px;background:var(--card);display:flex;align-items:center;justify-content:center;font-size:19px;font-weight:700;color:#2b2b2b;text-align:center;padding:0 14px}
.scrollbar{position:absolute;left:785px;top:262px;width:6px;height:335px;background:#ddd}
.scrollbar span{position:absolute;left:-2px;top:82px;width:10px;height:34px;background:#fff;border:1px solid #ccc;border-radius:3px}
.footer{position:absolute;left:0;top:640px;width:858px;height:174px;background:var(--brand);color:#fff}
.footer h3{position:absolute;top:32px;font-size:12px;font-weight:500}
.footer p,.footer li{font-size:8px;line-height:12.2px;font-weight:300;list-style:none}
.f-about{position:absolute;left:59px;top:63px;width:205px}
.f-links{position:absolute;left:322px;top:63px}
.f-states-a{position:absolute;left:466px;top:63px}
.f-states-b{position:absolute;left:558px;top:63px}
.footer li{line-height:14px}
.footer li::before{content:"› ";}
.f-contact{position:absolute;left:690px;top:63px;font-size:8px;font-weight:300}
.f-row{display:flex;gap:8px;align-items:flex-start;margin-bottom:10px}
.f-row svg{flex:none}
.f-phone{font-size:12px;font-weight:400}
.bottom-bar{position:absolute;left:0;top:814px;width:858px;height:50px;background:var(--bottom-bar);font-size:8px;color:#555;text-align:center;line-height:50px}
.shade{position:absolute;inset:0;background:var(--shade)}
.lightbox{position:absolute;left:261px;top:232px;width:340px;height:314px;background:#fff;border-radius:2px;padding:0 20px}
.close{position:absolute;left:332px;top:-12px;width:23px;height:23px}
.company-logo{position:absolute;left:22px;top:32px;width:107px;height:68px;border:1px solid #e2e2e2;display:flex;align-items:center;justify-content:center;font-size:14px;font-weight:700;color:var(--accent)}
.details{position:absolute;left:148px;top:34px;font-size:7.5px;color:#444}
.details .label{font-weight:700;font-size:7.5px;display:flex;gap:3px;align-items:center;color:#222}
.details .item{margin-bottom:8px}
.details .value{margin-top:3px}
.lightbox h2{position:absolute;left:20px;top:113px;font-size:11.5px;font-weight:500;color:var(--brand-text)}
.about{position:absolute;left:20px;top:133px;width:300px;font-size:8.1px;line-height:11.7px;color:#555;text-align:justify}
.about p+p{margin-top:11px}
.lightbox h4{position:absolute;left:20px;top:235px;font-size:11px;font-weight:500;color:var(--brand-text)}
.contact{position:absolute;top:256px;font-size:7.3px;line-height:11.5px;color:#444}
.contact strong{font-weight:700;color:#222}
.contact a{color:var(--accent);text-decoration:none}
</style>
</head>
<body>
<div class="site">
  <header class="header">
    <div class="brand"><span class="brand-mark"></span>Handwerkplatz.at</div>
    <nav class="nav"><a class="active" href="#">Home</a><a href="#">About Us</a><a href="#">Contact Us</a></nav>
  </header>

  <section class="hero" role="img" aria-label="City skyline photo at sunset">
    <h1>Welcome <span class="script">to</span> Handwerkplatz.at</h1>
    <p>Lorem Ipsum is simply dummy text of the printing and typesetting industry. Lorem Ipsum has been the industry's standard dummy text ever since the 1500s, when an unknown printer took a galley of type and specimen book.</p>
  </section>

  <form class="filter">
    <label>Short By</label>
    <div class="select">Austria</div>
    <div class="select">Burgenland</div>
    <div class="submit">Submit ➤</div>
  </form>

  <div class="grid">
    <div class="card">Brightline Media</div>
    <div class="card">Westhill Print</div>
    <div class="card">Roadside Signs Co</div>
    <div class="card">Nordwerk</div>
    <div class="card">Plakat Plus</div>
    <div class="card">Loop Studio</div>
    <div class="card">Adboard Group</div>
    <div class="card">Alpine Marketing Society</div>
    <div class="card">CineMotion</div>
  </div>
  <div class="scrollbar"><span></span></div>

  <footer class="footer">
    <h3 style="left:59px">About Us</h3>
    <p class="f-about">Lorem ipsum is simply dummy text of the printing and typesetting industry. Lorem Ipsum has been the industry's standard dummy text ever since the 1500s, when an unknown printer took a galley of type and scrambled it to make a type specimen book. It has survived not only five centuries, but also the leap into</p>
    <h3 style="left:322px">Quick Links</h3>
    <ul class="f-links"><li>Home</li><li>About Us</li><li>Clients</li><li>Privacy Policy</li><li>Contact Us</li></ul>
    <h3 style="left:466px">Austrian States</h3>
    <ul class="f-states-a"><li>Vienna</li><li>Lower Austria</li><li>Upper Austria</li><li>Styria</li><li>Tyrol</li></ul>
    <ul class="f-states-b"><li>Salzburg</li><li>Carinthia</li><li>Vorarlberg</li><li>Burgenland</li></ul>
    <h3 style="left:690px">Contact Us</h3>
    <div class="f-contact">
      <div class="f-row"><svg width="10" height="10" viewBox="0 0 10 10"><rect x="1" y="3" width="8" height="7" fill="#fff"/><rect x="3" y="0" width="4" height="4" fill="#fff"/></svg><span>4820 Linden Street<br>Graz 8010</span></div>
      <div class="f-row f-phone"><svg width="8" height="12" viewBox="0 0 8 12"><rect x="0.5" y="0.5" width="7" height="11" rx="1" fill="none" stroke="#fff"/></svg><span>316-472-0188</span></div>
      <div class="f-row"><svg width="10" height="8" viewBox="0 0 10 8"><rect width="10" height="8" fill="#fff"/><path d="M0 0l5 4 5-4" stroke="#3a8fc4" fill="none"/></svg><span>contact@handwerkplatz.at</span></div>
    </div>
  </footer>
  <div class="bottom-bar">Copyright © 2015 Handwerkplatz.at &nbsp;|&nbsp; Privacy Policy &nbsp;|&nbsp; Terms Of Use</div>

  <div class="shade"></div>

  <div class="lightbox" role="dialog" aria-label="Company details">
    <svg class="close" viewBox="0 0 23 23"><circle cx="11.5" cy="11.5" r="11.5" fill="#e02a2a"/><path d="M7.5 7.5l8 8M15.5 7.5l-8 8" stroke="#fff" stroke-width="2"/></svg>
    <div class="company-logo">Screenhall</div>
    <div class="details">
      <div class="item">
        <div class="label"><svg width="6" height="8" viewBox="0 0 6 8"><path d="M3 0a3 3 0 0 1 3 3c0 2-3 5-3 5S0 5 0 3a3 3 0 0 1 3-3z" fill="#222"/><circle cx="3" cy="3" r="1" fill="#fff"/></svg>ADDRESS</div>
        <div class="value">Donaulände 214, 4020 Linz</div>
      </div>
      <div class="item">
        <div class="label"><svg width="6" height="9" viewBox="0 0 6 9"><rect x="0.5" y="0.5" width="5" height="8" rx="1" fill="none" stroke="#222"/></svg>+43 732 418 506</div>
      </div>
      <div class="item">
        <div class="label"><svg width="8" height="8" viewBox="0 0 8 8"><circle cx="4" cy="4" r="4" fill="#222"/><path d="M0 4h8M4 0v8" stroke="#fff" stroke-width=".7"/></svg>WEBSITE</div>
        <div class="value">www.screenhall.at</div>
      </div>
    </div>
    <h2>Screenhall</h2>
    <div class="about">
      <p>SCREENHALL is the only Austrian cinema advertising company with 100% coverage of multiplex screens and operates a Digital Signage circuit of more than 700 TV screens in lobbies, concessions and box office of the main theaters of the country.</p>
      <p>We provide clients with the unique benefits that only cinema can offer, using high quality state of the art 2D and 3D digital technology and 35mm.</p>
    </div>
    <h4>Key contacts</h4>
    <div class="contact" style="left:20px"><strong>LENA HOFER</strong><br>Key Account Manager<br><a href="#">lhofer@screenhall.at</a></div>
    <div class="contact" style="left:135px"><strong>MARIE STADLER</strong><br>General Director<br><a href="#">marie@screenhall.at</a></div>
  </div>
</div>
</body>
</html>
```